" Atendimento médico em consultório/Clinica para mulheres em geral. A clinica contará com três médicas ginecologistas. Inicialmente somente a Dra. Lívia atenderá. O principal valor da Clinica é com o cuidado com a Mulher através de atendimento individual e cuidadoso através de especialistas nas áreas da ginecologia e Obstetricia. Apesar de possuir atendimento Obstétrico, o mesmo não será o principal foco da clinica. "

```html
<!DOCTYPE html>
<html lang="pt-BR">
<head>
<meta charset="utf-8">
<title>Receituário – Ginecologia Aurora</title>
<link rel="stylesheet" href="https://fonts.googleapis.com/css2?family=Cormorant+Garamond:wght@400;500&family=Arimo:wght@400;700&display=swap">
<style>
  :root{
    --backdrop:#e9eaeb;
    --paper:#ffffff;
    --rose:#e0676f;
    --rose-soft:#ec9aa0;
    --grey-text:#6f6f6f;
    --grey-dark:#4a4a4a;
    --watermark:#f3f3f3;
    --serif:"Cormorant Garamond", Georgia, serif;
    --sans:"Arimo", Arial, sans-serif;
  }
  *{margin:0;padding:0;box-sizing:border-box}
  html,body{width:1200px;height:1200px;overflow:hidden;background:var(--backdrop)}
  .letterhead{
    position:absolute;left:211px;top:60px;width:778px;height:1080px;
    background:var(--paper);box-shadow:0 2px 10px rgba(0,0,0,.12);overflow:hidden;
  }
  .brand{position:absolute;left:40px;top:118px;width:224px;text-align:center;color:var(--rose)}
  .brand-name{font-family:var(--serif);font-weight:500;font-size:30px;line-height:1}
  .brand-doctor{font-family:var(--serif);font-size:18px;margin-top:8px;color:var(--rose)}
  .doctor{position:absolute;right:34px;top:92px;text-align:right}
  .doctor-name{font-family:var(--sans);font-weight:700;font-size:25px;color:var(--rose);line-height:1.1}
  .doctor-specialty{font-family:var(--sans);font-weight:700;font-size:16px;color:var(--grey-text);margin-top:3px}
  .doctor-crm{font-family:var(--sans);font-weight:700;font-size:11px;color:var(--grey-text);margin-top:2px}
  .accent-bar{position:absolute;right:0;top:92px;width:17px;height:60px;background:var(--rose)}
  .doc-title{position:absolute;left:304px;top:236px;font-family:var(--serif);font-size:30px;color:var(--grey-text);letter-spacing:.5px}
  .watermark{position:absolute;left:140px;top:200px;width:380px;height:670px;
    background:radial-gradient(ellipse at 50% 55%, var(--watermark) 0%, rgba(243,243,243,.6) 55%, rgba(255,255,255,0) 75%)}
  .footer{position:absolute;left:36px;right:36px;bottom:34px;display:flex;align-items:center;
    font-family:var(--sans);color:var(--grey-dark);font-size:14px;font-weight:700}
  .contact{display:flex;align-items:center;gap:8px}
  .contact + .contact{margin-left:26px}
  .contact-icon{width:20px;height:20px;flex:none}
  .contact-address{font-size:10.5px;line-height:1.35}
  .footer-band{position:absolute;left:0;right:0;bottom:0;height:16px;background:var(--rose-soft)}
</style>
</head>
<body>
<main class="letterhead">
  <div class="watermark" role="img" aria-label="Marca decorativa suave ao fundo da folha"></div>

  <div class="brand">
    <div class="brand-name">Ginecologia Aurora</div>
    <div class="brand-doctor">Dra. Lívia Moura Santos</div>
  </div>

  <div class="doctor">
    <div class="doctor-name">Dra. Lívia Moura Santos</div>
    <div class="doctor-specialty">Ginecologia e Obstetrícia</div>
    <div class="doctor-crm">CRM 100482</div>
  </div>
  <div class="accent-bar"></div>

  <h1 class="doc-title">RECEITUÁRIO</h1>

  <footer class="footer">
    <div class="contact">
      <svg class="contact-icon" viewBox="0 0 20 20"><circle cx="10" cy="10" r="10" fill="var(--rose)"/><path d="M7 5.5l1.6 0 .8 2.3-1.1.9a6 6 0 0 0 3 3l.9-1.1 2.3.8v1.6c0 .6-.5 1-1.1 1A8 8 0 0 1 6 6.6c0-.6.4-1.1 1-1.1z" fill="#fff"/></svg>
      <span>(19) 3100-2040 / 3100-2041</span>
    </div>
    <div class="contact">
      <svg class="contact-icon" viewBox="0 0 20 20"><circle cx="10" cy="10" r="10" fill="var(--rose)"/><path d="M7 5.5l1.6 0 .8 2.3-1.1.9a6 6 0 0 0 3 3l.9-1.1 2.3.8v1.6c0 .6-.5 1-1.1 1A8 8 0 0 1 6 6.6c0-.6.4-1.1 1-1.1z" fill="#fff"/></svg>
      <span>(19) 98000-1234</span>
    </div>
    <div class="contact">
      <svg class="contact-icon" viewBox="0 0 20 20"><circle cx="10" cy="10" r="10" fill="var(--rose)"/><path d="M10 4.5a3.6 3.6 0 0 0-3.6 3.6c0 2.7 3.6 6.9 3.6 6.9s3.6-4.2 3.6-6.9A3.6 3.6 0 0 0 10 4.5zm0 5a1.4 1.4 0 1 1 0-2.8 1.4 1.4 0 0 1 0 2.8z" fill="#fff"/></svg>
      <span class="contact-address">Rua das Acácias, 150 5º Andar Conj52 Jd. Flores<br>Ed. Horizonte Center - 13000-000 Campinas-SP</span>
    </div>
  </footer>
  <div class="footer-band"></div>
</main>
</body>
</html>
```